Single page Web Application UI Design - Kendo UI / Angular2

We are in need of an application UI Design for a single web application page. We currently have a web based .net application that we are upgrading using Kendo UI and Angular. We have completed the wire frame and some of the functionality but we are now in need of a designer to provide an upgraded look/feel to the page.
The project will be two phases, with possible future ongoing hourly work depending on results.
Phase 1:
Take the current provided application page and create a design update for the panels, buttons, colors, etc. The output should be an HTML page. The underlying application code will use Kendo UI controls on Angular.
Phase 2:
Once we have decided on a final design we will need 10 color/skin variations designed. We will take the 10 skins and code them into css layers in Kendo for user selected skin changes. The output of this phase will be 10 HTML pages with images/colors to support the css layers development.
Access/login information:
1. Please open a browser to the following link:
http://198.51.100.27/LedgerScope_VDemo
2. Login with the following credentials:
Login: Design
Pass: Sketch7
3. Once logged in paste the following URL link into your browser:
http://198.51.100.27/LedgerScope_vDemo/FirstWave/ReviewFile/418096/QP7BD384KM2Rt
Any questions, concerns, or suggestions please contact us directly at: support@korvelbyte.example
Thank you,
Tobin
Target Market(s)
Healthcare claim auditors
Number of Pages Required
1 page
Look and feel

```html
<!DOCTYPE html>
<html lang="en">
<head>
<meta charset="utf-8">
<title>LedgerScope – Open Samples</title>
<link href="https://fonts.googleapis.com/css2?family=Arimo:wght@400;500;700&display=swap" rel="stylesheet">
<style>
:root{
  --green:#84c12a;
  --green-dark:#78b322;
  --filter-row:#d8ecb6;
  --row:#e8f6d4;
  --ink:#222;
  --muted:#555;
  --line:#e2e2e2;
  --band:#f7f7f7;
  --info-bg:#eef8f9;
  --info-line:#cfe8ec;
  --info-icon:#6ccbdc;
  --white:#fff;
}
*{box-sizing:border-box;margin:0;padding:0}
html,body{width:1200px;height:923px;overflow:hidden;background:var(--white)}
body{position:relative;font-family:"Arimo",Helvetica,Arial,sans-serif;color:var(--ink);font-size:13px}
.abs{position:absolute}

/* header */
.topbar{position:absolute;left:0;top:0;width:1200px;height:55px;background:var(--white);box-shadow:0 1px 3px rgba(0,0,0,.06)}
.brand{left:74px;top:15px;font-size:22px;color:#333;display:flex;align-items:center;gap:6px;font-weight:400}
.brand-mark{width:12px;height:12px;background:var(--green)}
.nav a{position:absolute;top:21px;font-size:13px;font-weight:500;color:#222;text-decoration:none;letter-spacing:.2px}
.nav a.active{color:var(--green)}
.nav .caret{display:inline-block;vertical-align:middle;margin-left:6px}
.user{left:974px;top:11px;display:flex;align-items:center;gap:10px;font-size:13.5px;font-weight:500}
.avatar{width:30px;height:30px;border-radius:50%;background:radial-gradient(circle at 50% 40%,#c9a68a,#6d5a4a)}
.user .tri{width:0;height:0;border-left:4px solid transparent;border-right:4px solid transparent;border-top:4px solid var(--green);margin-left:2px}

/* search band */
.searchband{position:absolute;left:0;top:55px;width:1200px;height:56px;background:var(--band)}
.label{font-size:13.5px;color:#222}
.field{height:30px;background:var(--white);border:1px solid var(--line);font-size:13.5px;color:#666;padding:6px 10px}
.btn{background:var(--green);color:var(--white);font-size:13px;font-weight:500;letter-spacing:.4px;display:flex;align-items:center;justify-content:center;gap:8px;text-transform:uppercase}

/* tabs */
.tabband{position:absolute;left:0;top:111px;width:1200px;height:49px;background:var(--green);border-top:3px solid var(--green-dark)}
.tab{position:absolute;top:15px;height:34px;background:#8fca38;color:var(--white);font-size:13.5px;display:flex;align-items:center;justify-content:center;border-radius:3px 3px 0 0}
.tab.active{top:11px;height:38px;background:var(--white);color:#222}

.title{left:73px;top:223px;font-size:23px;font-weight:400;color:#222}
.info{left:74px;top:266px;width:1051px;height:36px;background:var(--info-bg);border:1px solid var(--info-line);display:flex;align-items:center;padding-left:13px;gap:9px;font-size:13.5px;color:#333}
.info .dot{width:18px;height:18px;border-radius:50%;background:var(--info-icon);color:var(--white);font-size:12px;font-weight:700;display:flex;align-items:center;justify-content:center}

/* grid */
.grid{position:absolute;left:74px;top:317px;width:1052px;border-collapse:collapse;table-layout:fixed}
.grid th{background:var(--green);color:var(--white);text-align:left;font-weight:500;font-size:13px;height:38px;padding:0 13px;border-right:1px solid rgba(255,255,255,.35)}
.grid .filters td{background:var(--filter-row);height:49px;padding:0 13px;border-right:1px solid var(--white)}
.grid tbody.rows td{background:var(--row);height:47px;padding:0 13px;font-size:12.5px;border-right:1px solid var(--white);border-bottom:2px solid var(--white)}
.grid th:first-child,.grid td:first-child{padding:0;text-align:center}
.filter{display:flex;align-items:center;gap:10px}
.filter span{display:block;height:33px;background:var(--white);border:1px solid #a8d46a}
.check{display:inline-block;width:12px;height:12px;border:1px solid #8a8a8a;border-radius:2px;background:var(--white)}

.pager{left:74px;top:641px;width:1052px;height:44px;background:var(--green);display:flex;align-items:center;justify-content:flex-end;padding-right:11px;color:var(--white);font-size:13.5px;gap:8px}
.pager .page{width:36px;height:26px;background:var(--white);color:#222;border-radius:3px;padding:5px 10px;margin:0 2px}
.pager .circ{width:25px;height:25px;border-radius:50%;border:2px solid var(--white);display:flex;align-items:center;justify-content:center}
</style>
</head>
<body>

<header class="topbar">
  <div class="abs brand"><span>ledgerscope</span><span class="brand-mark"></span></div>
  <nav class="nav">
    <a class="active" style="left:278px" href="#">HOME</a>
    <a style="left:378px" href="#">SAMPLE<svg class="caret" width="11" height="7" viewBox="0 0 11 7"><path d="M1 1l4.5 4.5L10 1" fill="none" stroke="#222" stroke-width="1.6"/></svg></a>
    <a style="left:493px" href="#">ERROR</a>
    <a style="left:602px" href="#">FLAG</a>
    <a style="left:697px" href="#">ADMIN</a>
  </nav>
  <div class="abs user"><div class="avatar" role="img" aria-label="User profile photo"></div><span>Marlon Vesk</span><span class="tri"></span></div>
</header>

<section class="searchband">
  <span class="abs label" style="left:74px;top:20px">Application</span>
  <div class="abs field" style="left:155px;top:12px;width:203px">Select an option
    <svg style="position:absolute;right:10px;top:12px" width="9" height="6" viewBox="0 0 9 6"><path d="M1 1l3.5 3.5L8 1" fill="none" stroke="var(--green)" stroke-width="1.4"/></svg>
  </div>
  <span class="abs label" style="left:378px;top:20px">Claim Number</span>
  <div class="abs field" style="left:481px;top:12px;width:202px">Select an option</div>
  <div class="abs btn" style="left:702px;top:12px;width:129px;height:30px">
    <svg width="14" height="14" viewBox="0 0 14 14"><circle cx="8.5" cy="5.5" r="3.8" fill="none" stroke="#fff" stroke-width="2"/><path d="M5.7 8.3L1.5 12.5" stroke="#fff" stroke-width="2.4"/></svg>Search
  </div>
</section>

<div class="tabband">
  <div class="tab active" style="left:74px;width:115px">Open Samples</div>
  <div class="tab" style="left:203px;width:133px">Auditor Allocation</div>
  <div class="tab" style="left:345px;width:132px">My Open Claims</div>
  <div class="tab" style="left:487px;width:132px">My Second Audits</div>
  <div class="tab" style="left:629px;width:96px">My Errors</div>
  <div class="tab" style="left:735px;width:113px">Open Appeals</div>
  <div class="tab" style="left:858px;width:132px">My Closed Claims</div>
  <div class="tab" style="left:1000px;width:123px">Internal Auditing</div>
</div>

<div class="abs btn" style="left:765px;top:179px;width:156px;height:31px">Export to XLS</div>
<div class="abs btn" style="left:931px;top:179px;width:193px;height:31px">Add / Remove Fields</div>

<h1 class="abs title">Open Samples</h1>
<div class="abs info"><span class="dot">!</span>Drag a column header here to group by that column</div>

<svg width="0" height="0" style="position:absolute"><defs><symbol id="funnel" viewBox="0 0 20 18"><path d="M0 0h20v3.5l-7 6.5v8h-6v-8l-7-6.5z" fill="#6fae1f"/></symbol></defs></svg>

<table class="grid">
  <colgroup><col style="width:31px"><col style="width:163px"><col style="width:230px"><col style="width:111px"><col style="width:120px"><col style="width:140px"><col style="width:129px"><col style="width:128px"></colgroup>
  <thead>
    <tr><th><span class="check"></span></th><th>Sample ID</th><th>Sample Name</th><th>Total Claims</th><th>Active Claims</th><th>Unallocated Claims</th><th>Number of Errors</th><th>Open Errors</th></tr>
    <tr class="filters">
      <td></td>
      <td><div class="filter"><span style="width:106px"></span><svg width="19" height="17"><use href="#funnel"/></svg></div></td>
      <td><div class="filter"><span style="width:176px"></span><svg width="19" height="17"><use href="#funnel"/></svg></div></td>
      <td><div class="filter"><span style="width:55px"></span><svg width="19" height="17"><use href="#funnel"/></svg></div></td>
      <td><div class="filter"><span style="width:65px"></span><svg width="19" height="17"><use href="#funnel"/></svg></div></td>
      <td><div class="filter"><span style="width:83px"></span><svg width="19" height="17"><use href="#funnel"/></svg></div></td>
      <td><div class="filter"><span style="width:74px"></span><svg width="19" height="17"><use href="#funnel"/></svg></div></td>
      <td><div class="filter"><span style="width:74px"></span><svg width="19" height="17"><use href="#funnel"/></svg></div></td>
    </tr>
  </thead>
  <tbody class="rows">
    <tr><td><span class="check"></span></td><td>3877</td><td>9</td><td>9</td><td>12</td><td>15</td><td>0</td><td>0</td></tr>
    <tr><td><span class="check"></span></td><td>3877</td><td>9</td><td>9</td><td>12</td><td>15</td><td>0</td><td>0</td></tr>
    <tr><td><span class="check"></span></td><td>3877</td><td>9</td><td>9</td><td>12</td><td>15</td><td>0</td><td>0</td></tr>
    <tr><td><span class="check"></span></td><td>3877</td><td>9</td><td>9</td><td>12</td><td>15</td><td>0</td><td>0</td></tr>
    <tr><td><span class="check"></span></td><td>3877</td><td>9</td><td>9</td><td>12</td><td>15</td><td>0</td><td>0</td></tr>
  </tbody>
</table>

<div class="abs pager">
  <span>Page</span><span class="page">1</span><span>of 41</span>
  <span class="circ"><svg width="13" height="9" viewBox="0 0 13 9"><path d="M6 0v9L0 4.5zM13 0v9L7 4.5z" fill="#fff"/></svg></span>
  <span class="circ"><svg width="13" height="9" viewBox="0 0 13 9"><path d="M0 0v9l6-4.5zM7 0v9l6-4.5z" fill="#fff"/></svg></span>
</div>

</body>
</html>
```